Eco friendly Swedish beauty products sold in aluminum bottles - label design needed

We need help in designing a series of stick on labels for 80 ml (2.7 fl. oz.) aluminum bottles containing beauty products such as soaps, shampoo etc. The diameter of the bottle is 36 mm and the body of the bottles measures approx. 106 mm.
It is important for us that the label has a simplistic and clean feel with few colors (and the right ones!) and that the label helps amplify this product being both better and a more sustainable alternative to many of our plastic bottle competitors. The design and label should communicate the feel of an Eco-friendly, sustainable and modern brand of high quality - and with a Swedish concept.
We are using Montserrat font in our materials. Find attached information of preferred colors, the bottles and one example of our logotype. I am also available on e-mail should further information be needed.

Looking forward and very excited to receive your suggestions.
Note that we are expecting to start selling a series of approximately 10 different products where I will need one "master design" and then only smaller changes for each of the different products.

Target Market(s)

People whom are aware and not only look at price tag. Private and commercial market.

Industry/Entity Type

Beauty

Font styles to use
Other font styles liked:
• Montserrat

Requirements
Must have
• It must give the feel of being both better and a more sustainable alternative to many of our plastic bottle competitors.
Nice to have
• Simplistic. Clean. Clear.
Should not have
• Wrong colors, too complex designs.

```html
<!DOCTYPE html>
<html lang="en">
<head>
<meta charset="utf-8">
<title>Hair Shampoo Label</title>
<link rel="stylesheet" href="https://fonts.googleapis.com/css2?family=Montserrat:wght@400;500&family=Oswald:wght@500&family=Mrs+Saint+Delafield&display=swap">
<style>
  :root {
    --page: #ffffff;
    --sage: #b2b694;
    --tan: #d4ab7a;
    --graphite: #58595b;
    --olive: #6b7a3a;
    --white: #ffffff;
  }
  html, body {
    margin: 0;
    padding: 0;
    width: 1200px;
    height: 1200px;
    overflow: hidden;
    background: var(--page);
  }
  .canvas {
    position: relative;
    width: 1200px;
    height: 1200px;
  }
  .label {
    position: absolute;
    left: 0;
    top: 335px;
    width: 1200px;
    height: 530px;
    background: var(--sage);
    border-top: 8px solid var(--tan);
    border-bottom: 8px solid var(--tan);
    box-sizing: border-box;
    overflow: hidden;
  }
  .brand {
    position: absolute;
    top: 118px;
    left: 0;
    width: 100%;
    display: flex;
    justify-content: center;
    align-items: center;
    gap: 14px;
  }
  .brand-dot {
    width: 22px;
    height: 22px;
    border-radius: 50%;
    background: var(--graphite);
  }
  .brand-name {
    font-family: "Montserrat", sans-serif;
    font-weight: 400;
    font-size: 28px;
    letter-spacing: 2px;
    color: var(--graphite);
  }
  .brand-origin {
    position: absolute;
    top: 158px;
    left: 0;
    width: 100%;
    text-align: center;
    padding-left: 130px;
    box-sizing: border-box;
    font-family: "Montserrat", sans-serif;
    font-weight: 500;
    font-size: 10px;
    letter-spacing: 3px;
    color: var(--graphite);
  }
  .script-title {
    position: absolute;
    top: 190px;
    left: -20px;
    width: 1240px;
    text-align: center;
    font-family: "Mrs Saint Delafield", cursive;
    font-size: 230px;
    line-height: 1;
    color: var(--white);
    white-space: nowrap;
  }
  .product-name {
    position: absolute;
    top: 300px;
    left: 0;
    width: 100%;
    text-align: center;
    font-family: "Oswald", sans-serif;
    font-weight: 500;
    font-size: 26px;
    letter-spacing: 7px;
    color: var(--olive);
  }
  .volume {
    position: absolute;
    top: 478px;
    left: 0;
    width: 100%;
    text-align: center;
    font-family: "Montserrat", sans-serif;
    font-weight: 400;
    font-size: 19px;
    color: var(--olive);
  }
</style>
</head>
<body>
  <main class="canvas">
    <section class="label">
      <div class="brand">
        <span class="brand-dot"></span>
        <span class="brand-name">LINDVIK CARE</span>
      </div>
      <div class="brand-origin">SWEDEN</div>
      <div class="script-title">Hair Shampoo</div>
      <div class="product-name">Hair Shampoo</div>
      <div class="volume">80 ml</div>
    </section>
  </main>
</body>
</html>
```